Business card design for my trucking company

I would like a business card designed for my new trucking company. Please use my logo. the rest of the design is up to you. i would like my clients to say wow when they see the card. Im looking forward to seeing your designs

Target Market(s)

Industry/Entity Type

Trucking Company

Contact Information for Business Card

Marcus Tillbrook President
518-364-7120
ridgelinehaulage@examplemail.net

Font styles to use
Serif

Requirements
Must have
• my logo, name and number. we are located in Harrow Falls New York. the rest is up to you
Nice to have
• up to you
Should not have
• none

```html
<!DOCTYPE html>
<html lang="en">
<head>
<meta charset="utf-8">
<title>Ridgeline Haulage – Business Card</title>
<link href="https://fonts.googleapis.com/css2?family=Roboto:ital,wght@0,400;0,700;1,400;1,700&display=swap" rel="stylesheet">
<style>
  :root {
    --bg: #2b2b2d;
    --card-dark: #1f1f21;
    --card-light: #ffffff;
    --red: #e3222b;
    --grey: #555559;
    --grey-light: #8a8a8e;
  }
  * { margin: 0; padding: 0; box-sizing: border-box; }
  html, body { width: 1200px; height: 900px; overflow: hidden; background: var(--bg); }
  body { font-family: "Roboto", sans-serif; position: relative; }

  .card {
    position: absolute;
    left: 330px;
    width: 540px;
    height: 308px;
    border-radius: 4px;
    box-shadow: 0 14px 30px rgba(0,0,0,.45);
  }
  .card--front { top: 90px; background: var(--card-light); }
  .card--back  { top: 500px; background: var(--card-dark); display: flex; align-items: center; justify-content: center; }

  .brand { display: flex; align-items: center; gap: 10px; }
  .brand__dot { width: 14px; height: 14px; border-radius: 50%; background: var(--red); flex: none; }
  .brand__name { color: var(--red); font-weight: 700; font-size: 30px; letter-spacing: .5px; line-height: 1; }
  .brand__sub { color: var(--grey-light); font-weight: 700; font-size: 11px; letter-spacing: 2.2px; margin-top: 6px; text-transform: uppercase; }
  .card--back .brand__name { font-size: 44px; }
  .card--back .brand__sub { font-size: 15px; letter-spacing: 3px; }
  .card--back .brand__dot { width: 18px; height: 18px; }

  .card--front .brand-block { position: absolute; left: 30px; top: 112px; }
  .divider { position: absolute; left: 278px; top: 70px; width: 2px; height: 170px; background: var(--red); }

  .contact { position: absolute; left: 296px; top: 74px; color: var(--grey); }
  .contact__name { color: var(--red); font-weight: 700; font-style: italic; font-size: 20px; text-transform: uppercase; letter-spacing: .5px; }
  .contact__title { font-size: 14px; margin-top: 4px; }
  .contact__city { font-size: 14px; margin-top: 6px; }
  .contact__list { list-style: none; margin-top: 12px; }
  .contact__item { display: flex; align-items: center; gap: 7px; font-size: 13px; margin-bottom: 5px; white-space: nowrap; }
  .contact__icon { width: 12px; height: 12px; flex: none; fill: var(--red); }
</style>
</head>
<body>
  <section class="card card--front" aria-label="Business card front">
    <div class="brand-block">
      <div class="brand">
        <span class="brand__dot"></span>
        <span class="brand__name">RIDGELINE</span>
      </div>
      <div class="brand__sub">Haulage &amp; Logistics Inc.</div>
    </div>
    <div class="divider"></div>
    <div class="contact">
      <div class="contact__name">Marcus Tillbrook</div>
      <div class="contact__title">President</div>
      <div class="contact__city">Harrow Falls New York</div>
      <ul class="contact__list">
        <li class="contact__item">
          <svg class="contact__icon" viewBox="0 0 24 24"><path d="M6.6 10.8a15.1 15.1 0 0 0 6.6 6.6l2.2-2.2c.3-.3.7-.4 1-.2 1.1.4 2.3.6 3.6.6.6 0 1 .4 1 1V20c0 .6-.4 1-1 1A17 17 0 0 1 3 4c0-.6.4-1 1-1h3.5c.6 0 1 .4 1 1 0 1.3.2 2.5.6 3.6.1.3 0 .7-.2 1z"/></svg>
          518-364-7120
        </li>
        <li class="contact__item">
          <svg class="contact__icon" viewBox="0 0 24 24"><path d="M2 5h20v14H2z"/><path d="M2 5l10 7 10-7" fill="none" stroke="#fff" stroke-width="1.6"/></svg>
          ridgelinehaulage@examplemail.net
        </li>
        <li class="contact__item">
          <svg class="contact__icon" viewBox="0 0 24 24"><circle cx="12" cy="12" r="10"/><path d="M2 12h20M12 2c3 3 3 17 0 20M12 2c-3 3-3 17 0 20" fill="none" stroke="#fff" stroke-width="1.4"/></svg>
          www.ridgelinehaulage.net
        </li>
      </ul>
    </div>
  </section>

  <section class="card card--back" aria-label="Business card back">
    <div class="brand-block">
      <div class="brand">
        <span class="brand__dot"></span>
        <span class="brand__name">RIDGELINE</span>
      </div>
      <div class="brand__sub">Haulage &amp; Logistics Inc.</div>
    </div>
  </section>
</body>
</html>
```